Celling poster

It is a celling poster with questions that you ask yourself in the morning and a morning prayer + evening questions. People might put it on celling or on the wall.

Here is the contant, it is in Slovenian, but I have send you translation.

PO JUTRU SE DAN POZNA ...

1. Kaj me trenutno najbolj veseli v življenju?
3. Na kaj sem ponosna v življenju?
4. Za katere stvari danes čutim največ hvaležnosti?
5. V čem trenutno najbolj uživam?
6. Koga imam rada in kdo me ima rad?

Danes vstajam
s pomočjo nebeških sil:
svetlobe sonca,
sija lune,
žara ognja,
hitrosti strele,
okretnosti vetra,
globine morja,
stanovitnosti zemlje,
trdnosti skale.

VEČERNE MODROSTI

1. Kaj je bil danes moj prispevek svetu?
2. Kaj sem se danes naučila?
3. Katera situacija v dnevu mi je prinesla največ občutkov topline?

TRANSLATION for your understanding.

MORNING POWER QUESTIONS
1. What am I happy abou in my life right now?
2. What am I excited about in my life now?
3. What am I proud about in my life now?
4. What am I grateful about in my life now?
5. What am I enjoying most in my life now?
6. Who do I love? Who loves me?

MORNING PRAYER
Today I am waking up with the power of heavenly forces.
With the light of sun,
light of moon,
light of fire,
speed of lightning,
flexibility of wind,
depps of ocean,
stability of earth and
hardness of rock.

EVENING QUESTIONS OF WISDOM
1. What have I given today?
2. What did I learn today?
3. Which situations today gave me the most feelings of love, warmth?

```html
<!DOCTYPE html>
<html lang="sl">
<head>
<meta charset="utf-8">
<title>Po jutru se dan pozna – stropni plakat</title>
<link href="https://fonts.googleapis.com/css2?family=Amatic+SC:wght@700&family=Nunito+Sans:ital,wght@0,400;0,700;0,800;1,800&display=swap" rel="stylesheet">
<style>
  :root {
    --paper: #ffffff;
    --ink: #2b2b2b;
    --morning-pink: #d8266f;
    --evening-navy: #2f3184;
    --prayer-plum: #a51b5c;
    --wash-pink: #f6c6da;
    --wash-lilac: #d9c6ec;
    --wash-peach: #fbe0c8;
    --wash-blue: #cfe4f3;
    --panel-top: rgba(255,255,255,0.9);
    --panel-bottom: rgba(248,205,222,0.85);
  }
  * { margin: 0; padding: 0; box-sizing: border-box; }
  html, body { width: 900px; height: 1200px; overflow: hidden; }
  body {
    position: relative;
    font-family: "Nunito Sans", sans-serif;
    color: var(--ink);
    background:
      radial-gradient(ellipse 380px 140px at 140px 10px, var(--wash-peach), transparent 70%),
      radial-gradient(ellipse 300px 160px at 620px 30px, var(--wash-pink), transparent 70%),
      radial-gradient(ellipse 260px 200px at 880px 80px, var(--wash-lilac), transparent 70%),
      radial-gradient(ellipse 200px 300px at 900px 560px, var(--wash-blue), transparent 70%),
      var(--paper);
  }
  .poster-title {
    font-family: "Amatic SC", cursive;
    font-weight: 700;
    text-transform: uppercase;
    letter-spacing: 2px;
    line-height: 1;
    position: absolute;
    left: 62px;
  }
  .morning-title { top: 142px; font-size: 60px; color: var(--morning-pink); }
  .evening-title { top: 532px; font-size: 62px; color: var(--evening-navy); }
  .question-list {
    position: absolute;
    left: 62px;
    list-style: none;
    font-size: 25px;
    line-height: 40px;
  }
  .question-list em { font-style: italic; font-weight: 800; }
  .question-list .num { display: inline-block; width: 26px; }
  .question-list .indent { padding-left: 32px; }
  .morning-list { top: 229px; }
  .morning-list .num { font-weight: 800; }
  .evening-list { top: 622px; }
  .prayer-panel {
    position: absolute;
    left: 607px; top: 128px;
    width: 241px; height: 695px;
    border-radius: 36px;
    background: linear-gradient(180deg, var(--panel-top) 0%, var(--panel-bottom) 100%);
    text-align: center;
  }
  .prayer-title {
    font-family: "Amatic SC", cursive;
    font-weight: 700;
    text-transform: uppercase;
    color: var(--prayer-plum);
    font-size: 54px;
    line-height: 66px;
    letter-spacing: 2px;
    margin-top: 40px;
  }
  .prayer-text {
    margin-top: 28px;
    font-size: 24px;
    line-height: 39.6px;
  }
  .meadow {
    position: absolute;
    left: 0; bottom: 0;
    width: 900px; height: 360px;
    background:
      radial-gradient(ellipse 420px 220px at 180px 330px, var(--wash-pink), transparent 75%),
      radial-gradient(ellipse 420px 220px at 560px 320px, var(--wash-lilac), transparent 75%),
      linear-gradient(180deg, rgba(255,255,255,0) 0%, rgba(240,200,225,0.7) 100%);
  }
</style>
</head>
<body>
  <h1 class="poster-title morning-title">Po jutru se dan pozna</h1>
  <ol class="question-list morning-list">
    <li><span class="num">1.</span> Kaj me trenutno najbolj <em>veseli</em> v življenju?</li>
    <li><span class="num">3.</span> Na kaj sem <em>ponosna</em> v življenju?</li>
    <li><span class="num">4.</span> Za katere stvari danes čutim</li>
    <li class="indent">največ <em>hvaležnosti</em>?</li>
    <li><span class="num">5.</span> V čem trenutno <em>najbolj</em> uživam?</li>
    <li><span class="num">6.</span> Koga imam <em>rada</em> in kdo me ima <em>rad</em>?</li>
  </ol>

  <h2 class="poster-title evening-title">Večerne modrosti</h2>
  <ol class="question-list evening-list">
    <li><span class="num">1.</span> Kaj je bil danes moj <em>prispevek</em> svetu?</li>
    <li><span class="num">2.</span> Kaj sem se danes <em>naučila</em>?</li>
    <li><span class="num">3.</span> Katera situacija v dnevu mi je prinesla</li>
    <li class="indent">največ <em>občutkov</em> topline?</li>
  </ol>

  <aside class="prayer-panel">
    <h2 class="prayer-title">Jutranja<br>molitev</h2>
    <p class="prayer-text">
      Danes vstajam<br>s pomočjo<br>nebeških sil:<br>svetlobe sonca,<br>sija lune,<br>žara ognja,<br>hitrosti strele,<br>okretnosti vetra,<br>globine morja,<br>stanovitnosti<br>zemlje,<br>trdnosti skale.
    </p>
  </aside>

  <div class="meadow" role="img" aria-label="Line drawing of wildflowers, pansies, grasses and leafy sprigs over a pink and lilac watercolour wash"></div>
</body>
</html>
```